Poster/flyer design needed for Choral Concert

Please include the following text:<br/>Title of Event: Voices Aloft!<br/>Subtitle: A Choral Festival of Song to celebrate Kinship Fortnight<br/>Merriwade choirs come together to share their unique and beautiful music.<br/>Date: Sat March 21st 2020<br/>Time: 2pm - 4pm<br/>Venue: Tellbury Hall of Crafts<br/>Tickets: $10 each. Proceeds to Farm Relief & BVF Trust<br/>Hosted By Lifted Chords<br/>Featuring:<br/>Belvoran A Capella Women's Choir<br/>Bread of Song<br/>Merriwade Community Choir<br/>Chant Together<br/>* design required for A4 poster and DL flyer (may be modified)<br/>* Please use orange as the main colour<br/>* The Kinship fortnight logo must be included (see attached - either is fine). The frame may be useful as well.<br/>* Please include musical images<br/>* Visit kinshipfortnight.example.au for info on Kinship Fortnight

Target Market(s)

music-lovers, community-minded people, residents of the area, probably 30 + age

Industry/Entity Type

Entertainment

Font styles to use
Serif
Sans Serif

Colors
f78f20
ffffff

Requirements
Must have
• Orange colour
• Kinship logo
• required text
Nice to have
• A musical theme
Should not have
• writing should not be too small and difficult to read

```html
<!DOCTYPE html>
<html lang="en">
<head>
<meta charset="utf-8">
<title>Voices Aloft! – Kinship Fortnight Choral Festival</title>
<link href="https://fonts.googleapis.com/css2?family=Anton&family=Bebas+Neue&family=Great+Vibes&family=Oswald:wght@500;600&family=Quicksand:wght@500;700&family=Roboto+Condensed:wght@700;900&family=Libre+Baskerville:wght@700&display=swap" rel="stylesheet">
<style>
  :root {
    --orange: #f78f20;
    --orange-deep: #e9751f;
    --rust: #c3541f;
    --brown: #6b2613;
    --brown-dark: #4a2413;
    --ink: #1a0f0a;
    --white: #ffffff;
  }
  * { margin: 0; padding: 0; box-sizing: border-box; }
  html, body { width: 871px; height: 1200px; overflow: hidden; background: var(--white); }
  .poster {
    position: relative;
    width: 871px; height: 1200px;
    overflow: hidden;
    background: linear-gradient(180deg, #b8682c 0%, #d77f2a 35%, var(--orange-deep) 55%, var(--orange) 100%);
  }
  .choir-photo {
    position: absolute; left: 0; top: 0; width: 871px; height: 420px;
    background:
      linear-gradient(180deg, rgba(140,70,25,0.55) 0%, rgba(190,110,40,0.35) 45%, rgba(215,128,42,0) 100%),
      linear-gradient(90deg, #c27a33 0%, #d89a45 30%, #c98a3c 60%, #b96f2f 100%);
  }
  .brand-mark {
    position: absolute; left: 80px; top: 82px;
    font-family: 'Roboto Condensed', sans-serif; font-weight: 900;
    font-size: 30px; letter-spacing: -0.5px; color: var(--white);
  }
  .title-script {
    position: absolute; left: 170px; top: 300px;
    font-family: 'Great Vibes', cursive; font-size: 165px; line-height: 1;
    color: var(--white); transform: rotate(-6deg); z-index: 2;
  }
  .title-block {
    position: absolute; left: 0; top: 414px; width: 871px; text-align: center;
    font-family: 'Anton', sans-serif; font-size: 262px; line-height: 1;
    letter-spacing: 4px;
    background: linear-gradient(180deg, #8e4a24 0%, #c15a22 55%, #e0662a 100%);
    -webkit-background-clip: text; background-clip: text; color: transparent;
  }
  .subtitle {
    position: absolute; left: 0; top: 648px; width: 871px; text-align: center;
    font-family: 'Bebas Neue', sans-serif; font-size: 39px; line-height: 37px;
    color: var(--ink); letter-spacing: 0.5px;
  }
  .lineup {
    position: absolute; left: 40px; top: 808px; width: 390px; text-align: center;
    font-family: 'Bebas Neue', sans-serif; color: var(--ink);
  }
  .lineup .label { font-size: 22px; line-height: 24px; }
  .lineup .host { font-size: 32px; line-height: 34px; margin-bottom: 12px; }
  .lineup ul { list-style: none; }
  .lineup li { font-size: 32px; line-height: 41px; }
  .lineup li::before {
    content: ""; display: inline-block; width: 0; height: 0; margin-right: 8px;
    border-left: 7px solid var(--ink); border-top: 6px solid transparent; border-bottom: 6px solid transparent;
    vertical-align: 8px;
  }
  .date-banner { position: absolute; left: 418px; top: 752px; width: 416px; height: 276px; }
  .date-text {
    position: absolute; left: 418px; top: 828px; width: 416px; text-align: center;
    font-family: 'Oswald', sans-serif; font-weight: 600; color: var(--white);
    font-size: 37px; line-height: 39px; letter-spacing: 0.3px;
  }
  .date-text sup { font-size: 18px; vertical-align: 18px; }
  .tickets {
    position: absolute; left: 470px; top: 1000px; width: 310px; text-align: center;
    font-family: 'Quicksand', sans-serif; color: var(--brown-dark);
  }
  .tickets .price { font-weight: 700; font-size: 24px; line-height: 30px; letter-spacing: 0.5px; }
  .tickets .cause { font-weight: 500; font-size: 19px; line-height: 23px; margin-top: 4px; }
  .footer {
    position: absolute; left: 0; top: 1108px; width: 871px; height: 92px; background: var(--white);
    display: flex; align-items: center; justify-content: space-around; padding: 0 60px;
  }
  .gov {
    display: flex; align-items: center; gap: 8px;
    font-family: 'Libre Baskerville', serif; font-weight: 700; font-size: 9px; line-height: 14px; color: var(--ink);
  }
  .gov .dot { width: 26px; height: 26px; border-radius: 50%; background: var(--ink); }
  .gov .rule { border-top: 1px solid var(--ink); }
  .tagline { font-family: 'Roboto Condensed', sans-serif; font-weight: 700; font-size: 24px; color: var(--ink); }
  .hashtag { font-family: 'Roboto Condensed', sans-serif; font-weight: 900; font-size: 24px; color: var(--ink); }
</style>
</head>
<body>
<main class="poster">
  <div class="choir-photo" role="img" aria-label="Photograph of a choir singing outdoors with a conductor, toned in orange"></div>

  <div class="brand-mark">KINSHIP FORTNIGHT</div>

  <div class="title-block">ALOFT!</div>
  <div class="title-script">Voices</div>

  <p class="subtitle">
    A Choral Festival of Song to celebrate Kinship Fortnight<br>
    Merriwade choirs come together to share<br>
    their unique and beautiful music.
  </p>

  <section class="lineup">
    <div class="label">Hosted by:</div>
    <div class="host">Lifted Chords</div>
    <div class="label">Featuring:</div>
    <ul>
      <li>Bread of Song</li>
      <li>Belvoran A Capella Women's Choir</li>
      <li>Merriwade Community Choir</li>
      <li>Chant Together</li>
    </ul>
  </section>

  <svg class="date-banner" viewBox="0 0 416 276" aria-hidden="true">
    <path d="M6 42 C120 70 260 50 404 2 C370 90 378 170 410 236 C290 226 150 232 12 274 C46 190 44 110 6 42 Z"
          fill="var(--brown)" stroke="var(--white)" stroke-width="6" stroke-linejoin="round"/>
  </svg>
  <div class="date-text">
    Saturday, March 21<sup>ST</sup><br>
    Tellbury Hall of Crafts<br>
    2PM - 4PM
  </div>

  <div class="tickets">
    <div class="price">TICKETS: $10 EACH</div>
    <div class="cause">Proceeds to Farm Relief<br>&amp; BVF Trust</div>
  </div>

  <footer class="footer">
    <div class="gov">
      <span class="dot"></span>
      <div><div>Northvale Government</div><div class="rule">Department of Civic Affairs</div></div>
    </div>
    <div class="tagline">ALL ARE WELCOME</div>
    <div class="hashtag">#kinshipfortnight</div>
  </footer>
</main>
</body>
</html>
```